BRV TAX & ACCOUNTING business card
Income tax, audit, bookkeeping, setup, training and services
Professional
Derek Lim Varga
48 Bexwell Drive
Toronto, ON M2K 4T8
brv_tax@quillmail.ca

```html
<!DOCTYPE html>
<html lang="en">
<head>
<meta charset="utf-8">
<title>BRV Tax &amp; Accounting – Business Card</title>
<link rel="stylesheet" href="https://fonts.googleapis.com/css2?family=Open+Sans:wght@400;600;800&display=swap">
<style>
  :root {
    --green: #7cc21f;
    --green-light: #a6d95a;
    --ink: #3a3a3a;
    --paper: #ffffff;
    --backdrop: #e6e7e8;
    --shadow: rgba(0, 0, 0, 0.18);
  }
  * { margin: 0; padding: 0; box-sizing: border-box; }
  html, body {
    width: 1200px; height: 864px; overflow: hidden;
    background: var(--backdrop);
    font-family: "Open Sans", Arial, sans-serif;
  }
  .sheet {
    width: 1200px; height: 864px;
    display: flex; align-items: center; justify-content: center; gap: 40px;
  }
  .card {
    position: relative;
    width: 540px; height: 310px;
    background: var(--paper);
    border-radius: 18px;
    overflow: hidden;
    box-shadow: 0 10px 28px var(--shadow);
  }
  .brand-name {
    color: var(--green);
    font-weight: 800;
    line-height: 1;
    text-transform: uppercase;
  }
  .brand-name .word { display: block; letter-spacing: -1px; }
  .brand-name .tagline { display: block; letter-spacing: 0.5px; }

  /* Front */
  .card--front .brand-name {
    position: absolute; left: 50%; top: 50%;
    transform: translate(-50%, -50%);
    text-align: left;
  }
  .card--front .word { font-size: 78px; }
  .card--front .tagline { font-size: 19px; margin-top: 6px; }

  /* Back */
  .card--back .wave { position: absolute; inset: 0; width: 540px; height: 310px; }
  .card--back .holder {
    position: absolute; right: 30px; top: 168px;
    color: var(--green); font-weight: 600; font-size: 17px;
  }
  .card--back .brand-name { position: absolute; left: 36px; top: 112px; }
  .card--back .word { font-size: 56px; }
  .card--back .tagline { font-size: 14px; margin-top: 4px; }
  .contact {
    position: absolute; left: 36px; top: 196px;
    list-style: none; color: var(--ink); font-size: 12px; line-height: 1.35;
  }
  .contact li { display: flex; align-items: flex-start; gap: 8px; margin-bottom: 3px; }
  .contact svg { flex: none; width: 13px; height: 13px; margin-top: 2px; }
</style>
</head>
<body>
<main class="sheet">
  <section class="card card--front">
    <div class="brand-name">
      <span class="word">BRV</span>
      <span class="tagline">Tax &amp; Accounting</span>
    </div>
  </section>

  <section class="card card--back">
    <svg class="wave" viewBox="0 0 540 310" aria-hidden="true">
      <path d="M0,0 H540 V150 C440,152 360,80 250,48 C160,22 80,14 0,12 Z" fill="var(--green-light)"/>
      <path d="M0,0 H540 V132 C440,132 360,64 250,34 C160,10 80,4 0,4 Z" fill="var(--green)"/>
    </svg>
    <p class="holder">Derek Lim Varga</p>
    <div class="brand-name">
      <span class="word">BRV</span>
      <span class="tagline">Tax &amp; Accounting</span>
    </div>
    <ul class="contact">
      <li>
        <svg viewBox="0 0 14 14"><circle cx="7" cy="7" r="7" fill="var(--green)"/><path d="M7 3a2.6 2.6 0 0 0-2.6 2.6C4.4 7.6 7 11 7 11s2.6-3.4 2.6-5.4A2.6 2.6 0 0 0 7 3zm0 3.6a1 1 0 1 1 0-2 1 1 0 0 1 0 2z" fill="#fff"/></svg>
        <span>48 Bexwell Drive<br>Toronto, ON M2K 4T8</span>
      </li>
      <li>
        <svg viewBox="0 0 14 14"><circle cx="7" cy="7" r="7" fill="var(--green)"/><path d="M4.6 3.6l1.3-.2.8 1.8-.9.7c.4.9 1.1 1.6 2 2l.7-.9 1.8.8-.2 1.3c-3 .3-5.8-2.5-5.5-5.5z" fill="#fff"/></svg>
        <span>416-555-0187</span>
      </li>
      <li>
        <svg viewBox="0 0 14 14"><circle cx="7" cy="7" r="7" fill="var(--green)"/><rect x="3.5" y="4.5" width="7" height="5" fill="#fff"/><path d="M3.5 4.5 7 7.3l3.5-2.8" stroke="var(--green)" stroke-width=".8" fill="none"/></svg>
        <span>brv_tax@quillmail.ca</span>
      </li>
      <li>
        <svg viewBox="0 0 14 14"><circle cx="7" cy="7" r="7" fill="var(--green)"/><circle cx="7" cy="7" r="3.6" stroke="#fff" stroke-width=".9" fill="none"/><path d="M3.4 7h7.2M7 3.4c-1.6 2-1.6 5.2 0 7.2M7 3.4c1.6 2 1.6 5.2 0 7.2" stroke="#fff" stroke-width=".7" fill="none"/></svg>
        <span>www.brvtaxcare.ca</span>
      </li>
    </ul>
  </section>
</main>
</body>
</html>
```